i would like a business card to leave with customers and potential customers for electrical work and for the supply and install of reverse cycle airconditioning in the domestic and commercial market.
I own my own business and im a sole trader. I have an a'class electrical lisence and also a refrigeration lisence so i am
able to offer complete installations in airconditioning by a fully qualified and lisenced tradesman.
im looking for something that comes across as unique and professional.
i had the coluor black and some gold in mind but open to any coluors.
something like Beacon Electrical & Refrigeration
or Beacon Air.
i will use this design on a business card to advertise through summer to help generate installs through the busy season.

Target Market(s)

Mainly domestic house holds through summer who are in need of airconditioning and reliable information to acomadate thier cooling and heating requirements

Industry/Entity Type

Electrical

Requirements
Must have
• Business name- Beacon
My name- Peter Wollaston
My mobile no- 0457 819 302
My email- prwollaston@tarvel.com.au
Installation & Decomissioning of aiconditioning split systems
LIC NO: KTR 407516
Nice to have
• Beacon Electrical & Refrigeration

```html
<!DOCTYPE html>
<html lang="en">
<head>
<meta charset="utf-8">
<title>Beacon Electrical &amp; Refrigeration – Business Card</title>
<link href="https://fonts.googleapis.com/css2?family=Arimo:ital,wght@0,400;0,700;1,700&family=Roboto+Condensed:ital,wght@1,700&display=swap" rel="stylesheet">
<style>
  :root {
    --ink: #111111;
    --text: #1c1c1c;
    --brand-blue: #1a6fb8;
    --band-blue: #1ea3e0;
    --icon-blue: #1b8fd6;
    --warm-sand: #f6d9a0;
    --cool-sky: #bfe3f6;
    --page: #ffffff;
    --frame: #2a2a2a;
  }
  html, body {
    margin: 0;
    width: 1200px;
    height: 900px;
    overflow: hidden;
    background: var(--page);
    font-family: "Arimo", Arial, sans-serif;
    color: var(--text);
  }
  .canvas { position: relative; width: 1200px; height: 900px; }
  .card {
    position: absolute;
    left: 170px; top: 186px;
    width: 850px; height: 514px;
    box-sizing: border-box;
    border: 2px solid var(--frame);
    background: var(--page);
    overflow: hidden;
  }
  .backdrop-wash {
    position: absolute;
    left: 300px; top: 0;
    width: 550px; height: 450px;
    background:
      radial-gradient(ellipse 60% 70% at 20% 40%, rgba(246,217,160,0.75), rgba(246,217,160,0) 70%),
      radial-gradient(ellipse 55% 70% at 85% 75%, rgba(191,227,246,0.9), rgba(191,227,246,0) 72%);
  }
  .brand { position: absolute; left: 46px; top: 42px; }
  .brand-mark {
    position: absolute; left: 0; top: 2px;
    width: 84px; height: 84px;
    background: var(--brand-blue);
  }
  .brand-name {
    position: absolute; left: 124px; top: -8px;
    margin: 0;
    font-weight: 700;
    font-size: 80px;
    line-height: 1;
    color: var(--ink);
    letter-spacing: -1px;
  }
  .brand-tagline {
    position: absolute; left: 308px; top: 110px;
    margin: 0;
    white-space: nowrap;
    font-weight: 700; font-style: italic;
    font-size: 27px;
    color: var(--brand-blue);
  }
  .owner-name {
    position: absolute; left: 46px; top: 218px;
    margin: 0;
    font-weight: 700; font-size: 30px;
    color: var(--ink);
  }
  .contact { position: absolute; left: 46px; top: 272px; margin: 0; padding: 0; list-style: none; }
  .contact-item { display: flex; align-items: center; height: 48px; }
  .contact-item svg { width: 32px; height: 32px; margin-right: 28px; flex: none; }
  .contact-phone { font-size: 28px; }
  .contact-email { font-size: 24px; }
  .licence {
    position: absolute; left: 38px; top: 405px;
    margin: 0; font-size: 22px;
  }
  .credentials {
    position: absolute; left: 400px; top: 282px;
    margin: 0; padding: 0; list-style: none;
    font-size: 23px;
  }
  .credentials li { position: relative; padding-left: 28px; height: 37px; }
  .credentials li::before {
    content: ""; position: absolute; left: 0; top: 7px;
    width: 13px; height: 13px; background: var(--ink);
  }
  .service-band {
    position: absolute; left: 0; bottom: 8px;
    width: 100%; height: 52px;
    background: var(--band-blue);
    display: flex; align-items: center; justify-content: center;
    margin: 0;
    font-family: "Roboto Condensed", "Arial Narrow", sans-serif;
    font-weight: 700; font-style: italic;
    font-size: 27px; color: #ffffff;
  }
</style>
</head>
<body>
<div class="canvas">
  <section class="card">
    <div class="backdrop-wash" role="img" aria-label="Soft warm-to-cool paint splash texture in sand and sky blue"></div>

    <header class="brand">
      <div class="brand-mark"></div>
      <h1 class="brand-name">Beacon</h1>
      <p class="brand-tagline">Electrical &amp; Refrigeration</p>
    </header>

    <h2 class="owner-name">Peter Wollaston</h2>

    <ul class="contact">
      <li class="contact-item contact-phone">
        <svg viewBox="0 0 32 32" aria-hidden="true">
          <rect x="8" y="2" width="16" height="28" rx="3" fill="var(--icon-blue)"/>
          <rect x="11" y="6" width="10" height="15" fill="#ffffff"/>
          <circle cx="16" cy="25.5" r="1.8" fill="#ffffff"/>
        </svg>
        0457 819 302
      </li>
      <li class="contact-item contact-email">
        <svg viewBox="0 0 32 32" aria-hidden="true">
          <rect x="2" y="7" width="28" height="19" fill="var(--icon-blue)"/>
          <polyline points="4,9 16,19 28,9" fill="none" stroke="#ffffff" stroke-width="2.5"/>
        </svg>
        prwollaston@tarvel.com.au
      </li>
    </ul>

    <p class="licence">Lic. No.: KTR 407516</p>

    <ul class="credentials">
      <li>Fully qualified</li>
      <li>A class electrical licence</li>
      <li>Refrigeration licence</li>
      <li>Complete air conditioning installations</li>
    </ul>

    <p class="service-band">Installation &amp; Decomissioning of Split Air Conditioning Systems</p>
  </section>
</div>
</body>
</html>
```